Website design improvement for existing site

We would like design ideas for how the inner pages (not the homepage) of www.quillbrookmedia.com could be improved. We don't want to totally redesign the website. We want to improve / enhance / develop it further to look high-end, sophisticated and visually stunning.

Target Market(s)

High end video production clients. National and international TV networks and brands wanting commercial filming.

Industry/Entity Type

Videography

Other font styles liked:
• Existing site fonts

Requirements
Must have
• Improvement on the existing inner pages without totally re-working the design. We want to achieve a high-end sophisticated look with the existing branding (colours, images etc)
Nice to have
• Any ideas for improving the homepage are also welcome but we are mostly happy with this page so it is not the priority.
Should not have
• Any major changes to colours, styles etc.

```html
<!DOCTYPE html>
<html lang="en">
<head>
<meta charset="utf-8">
<title>Quillbrook Media – Process</title>
<link href="https://fonts.googleapis.com/css2?family=Oswald:wght@500;600&family=Open+Sans:wght@400;600&display=swap" rel="stylesheet">
<style>
:root{
  --red:#dc1c1c;
  --black:#0b0b0b;
  --page:#f0f0f0;
  --white:#ffffff;
  --ink:#1a1a1a;
  --grey:#9a9a9a;
  --line:#111111;
}
*{box-sizing:border-box;margin:0;padding:0}
html,body{width:1200px;height:2206px;overflow:hidden}
body{position:relative;background:var(--page);font-family:"Open Sans",Arial,sans-serif;color:var(--ink)}
.abs{position:absolute}

/* header */
.site-nav{left:0;top:0;width:1200px;height:48px;background:var(--black)}
.brand{display:flex;align-items:center;gap:8px;color:var(--white);font-family:"Oswald",Arial,sans-serif;font-weight:500;font-size:19px;letter-spacing:.5px;white-space:nowrap}
.brand-dot{width:20px;height:20px;border-radius:50%;background:var(--red)}
.site-nav .brand{position:absolute;left:110px;top:11px}
.nav-links{position:absolute;top:17px;left:0;width:1200px;list-style:none}
.nav-links li{position:absolute;font-size:11px;letter-spacing:3px;color:#cfcfcf;font-weight:400}
.nav-links li.active{color:var(--red)}

/* hero */
.hero{left:0;top:48px;width:1200px;height:401px;border-bottom:3px solid var(--line)}
.hero-photo{width:100%;height:100%;
  background:
    radial-gradient(ellipse 260px 220px at 640px 210px,rgba(30,30,32,.75),rgba(30,30,32,0) 70%),
    radial-gradient(ellipse 320px 260px at 960px 150px,rgba(235,235,232,.55),rgba(235,235,232,0) 70%),
    radial-gradient(ellipse 300px 320px at 120px 260px,rgba(10,10,10,.9),rgba(10,10,10,0) 75%),
    linear-gradient(100deg,#1b1b1b 0%,#4a4744 32%,#7d7a75 55%,#a9a7a2 78%,#cfcecb 100%)}
.hero-kicker{left:144px;top:162px;color:var(--white);font-size:29px;letter-spacing:9px;font-weight:400}
.hero-line{left:144px;height:40px;padding:0 9px;color:var(--white);font-family:"Oswald",Arial,sans-serif;font-weight:500;font-size:33px;line-height:40px;white-space:nowrap}
.hero-line.dark{top:208px;background:var(--black)}
.hero-line.red{top:255px;background:var(--red)}

/* section marker: plain square */
.marker{width:26px;height:26px;margin-left:-13px;margin-top:-13px;background:var(--red);border:3px solid var(--line)}

/* cards */
.card{background:var(--white);box-shadow:0 1px 3px rgba(0,0,0,.08)}
.card-photo{position:absolute;top:0;width:440px;height:100%}
.card-title{position:absolute;font-size:20px;letter-spacing:2.4px;font-weight:600;border-left:4px solid var(--red);padding-left:8px;line-height:22px;white-space:nowrap}
.card-title.right{border-left:none;border-right:4px solid var(--red);padding-left:0;padding-right:8px;text-align:right}
.card-text{position:absolute;font-size:11.5px;line-height:19px;color:var(--grey)}

.story{left:160px;top:570px;width:879px;height:319px}
.story .card-photo{left:0;
  background:
    radial-gradient(ellipse 140px 160px at 90px 120px,rgba(90,80,70,.7),rgba(90,80,70,0) 70%),
    radial-gradient(ellipse 160px 200px at 360px 180px,rgba(20,20,20,.75),rgba(20,20,20,0) 70%),
    radial-gradient(ellipse 200px 90px at 220px 290px,rgba(205,160,105,.8),rgba(205,160,105,0) 70%),
    linear-gradient(180deg,#b7b1a6 0%,#8f8a82 45%,#a88a62 80%,#c9a274 100%)}

.plan-band{left:0;top:1011px;width:1200px;height:376px;border-top:3px solid var(--line);border-bottom:3px solid var(--line);background:var(--red)}
.plan-photo{position:absolute;left:0;top:0;width:600px;height:100%;
  background:
    radial-gradient(ellipse 160px 70px at 170px 210px,rgba(245,242,236,.9),rgba(245,242,236,0) 75%),
    radial-gradient(ellipse 120px 70px at 480px 230px,rgba(215,190,150,.8),rgba(215,190,150,0) 75%),
    linear-gradient(180deg,#3a322d 0%,#5a4c42 40%,#8a7462 62%,#b88f62 80%,#8f6a45 100%)}
.plan-band .card-title{color:var(--white);border-left-color:var(--white)}
.plan-band .card-text{color:var(--white)}

.audience{left:159px;top:1508px;width:880px;height:319px}
.audience .card-photo{left:440px;
  background:
    radial-gradient(ellipse 110px 130px at 70px 200px,rgba(20,20,20,.8),rgba(20,20,20,0) 70%),
    radial-gradient(ellipse 120px 80px at 260px 150px,rgba(210,205,200,.7),rgba(210,205,200,0) 70%),
    radial-gradient(ellipse 200px 80px at 260px 280px,rgba(210,160,100,.85),rgba(210,160,100,0) 70%),
    linear-gradient(180deg,#6b4a2c 0%,#8c6b4c 35%,#9a8b7c 60%,#b88c5c 100%)}

/* partners */
.partners{left:0;top:1914px;width:1200px;height:40px}
.partner{position:absolute;top:0;transform:translateX(-50%);display:flex;align-items:center;gap:8px;font-family:"Oswald",Arial,sans-serif;font-weight:500;font-size:22px;color:#555555;white-space:nowrap}
.partner .dot{width:14px;height:14px;border-radius:50%;background:var(--red)}

/* footer */
.site-footer{left:0;top:2033px;width:1200px;height:173px;background:var(--black);color:var(--white);text-align:center}
.site-footer .brand{position:absolute;left:50%;top:27px;transform:translateX(-50%)}
.footer-info{position:absolute;left:0;top:76px;width:100%;font-size:10.5px;letter-spacing:1.6px;line-height:16px;color:#d8d8d8}
.social{position:absolute;left:0;top:142px;width:100%;font-size:12px;font-weight:600;letter-spacing:1px;word-spacing:14px}
</style>
</head>
<body>

<header class="site-nav abs">
  <div class="brand"><span class="brand-dot"></span>QUILLBROOK MEDIA</div>
  <ul class="nav-links">
    <li style="left:547px">HOME</li>
    <li style="left:632px">ABOUT</li>
    <li class="active" style="left:726px">PROCESS</li>
    <li style="left:838px">BRAND STORIES</li>
    <li style="left:1012px">CONTACT</li>
  </ul>
</header>

<section class="hero abs">
  <div class="hero-photo" role="img" aria-label="Camera operator filming chefs in a busy commercial kitchen"></div>
</section>
<h1 class="hero-kicker abs">HOW WE DO IT.</h1>
<div class="hero-line dark abs">END-TO-END CREATIVE PROCESS.</div>
<div class="hero-line red abs">DISTINCTIVE OUTCOMES.</div>

<div class="marker abs" style="left:600px;top:449px" aria-hidden="true"></div>

<article class="story card abs">
  <div class="card-photo" role="img" aria-label="Film crew recording a baker kneading dough at a kitchen counter"></div>
  <h2 class="card-title" style="left:487px;top:40px">Our Experience Enable Us...</h2>
  <p class="card-text" style="left:487px;top:78px;width:350px">To quickly understand the nuance of your brand, vision and message. Our creativity brings it to life through story boarding, script and expert cinematography. And our post-production team produce the full and finished film.</p>
</article>

<section class="plan-band abs">
  <div class="plan-photo" role="img" aria-label="Close-up of a bowl and freshly baked bread on a wooden table"></div>
  <h2 class="card-title" style="left:671px;top:74px">We'll sit down you and...</h2>
  <p class="card-text" style="left:671px;top:112px;width:312px">Your team to work out your story. What's your vision? What's the narrative? Once you're happy with the concept, we will develop and plan the production. We will plan, shoot and get your story in the can. Post-production will add the final touches to the film.</p>
</section>

<div class="marker abs" style="left:600px;top:1011px" aria-hidden="true"></div>
<div class="marker abs" style="left:600px;top:1387px" aria-hidden="true"></div>

<article class="audience card abs">
  <h2 class="card-title right" style="right:480px;top:40px">Let's tell your audience</h2>
  <p class="card-text" style="right:480px;top:80px;width:338px;text-align:right">why you exist and what makes you get out of bed in the morning. Show them how it all began - the problem, the solution, and why you make the world a better place.</p>
  <p class="card-text" style="right:480px;top:162px;width:338px;text-align:right">Share your greatest asset. Showcase your people and what makes them awesome. Demonstrate your product and prove your value in the most compelling media.</p>
  <div class="card-photo" role="img" aria-label="Camera crew interviewing a smiling business owner in his kitchen workshop"></div>
</article>

<div class="partners abs">
  <div class="partner" style="left:207px"><span class="dot"></span>Northcast</div>
  <div class="partner" style="left:341px">Vista</div>
  <div class="partner" style="left:472px">Brightline</div>
  <div class="partner" style="left:619px">Fieldmark</div>
  <div class="partner" style="left:786px">Elmstone</div>
  <div class="partner" style="left:970px">Kestrel</div>
</div>

<footer class="site-footer abs">
  <div class="brand"><span class="brand-dot"></span>QUILLBROOK MEDIA</div>
  <p class="footer-info">01632 960418 | hello@quillbrookmedia.com<br>Company No. 12034567<br>VAT No. 318540927</p>
  <p class="social">Linkly Snapframe</p>
</footer>

</body>
</html>
```